Fiber Optic Internet flyer promotion Winter 2016-2017

I am looking for a marketing flyer that will not be folded, single sided that will advertise a Fiber Optic internet promotion that we are currently running.

The design should be clean, flow well, quickly grab attention, and if a very few short seconds list what the promotion is, and direct them to contact us.

It needs to list a few features of the promotion, but does not need to be in this order and should flow well with the flyer
1.) Fiber Optic Internet
2.) 100 Mbits for $140 /month or 150 Mbits for $190 /month
3.) Free construction cost up to $10,000, limited funds available.
4.) Limited time offer. Must commit before funds run out.

(555) 274-3619, www.kelvaroute.net

Target Market(s)

Small to large business

Industry/Entity Type

Internet Service Provider

Requirements
Must have
• Eye catching appeal. Quickly convey the message of the promotion and our company name and phone number.
Should not have
• Our company is primarily a wireless ISP. This promotion is all about Fiber Optic. I do not want to draw attention to the "wireless" portion of our business with this flyer.

```html
<!DOCTYPE html>
<html lang="en">
<head>
<meta charset="utf-8">
<title>Kelva Route Networks – Fiber Optic Internet Flyer</title>
<link href="https://fonts.googleapis.com/css2?family=Montserrat:wght@400;500;600;700;800&display=swap" rel="stylesheet">
<style>
  :root {
    --navy: #27306f;
    --navy-deep: #1f2760;
    --red: #c8202f;
    --red-deep: #9c1620;
    --red-soft: #d9534f;
    --white: #ffffff;
    --ink: #27306f;
    --photo-light: #e9eef4;
    --photo-mid: #bfcde0;
  }
  * { margin: 0; padding: 0; box-sizing: border-box; }
  html, body { width: 848px; height: 1200px; overflow: hidden; background: var(--white); }
  body { font-family: "Montserrat", sans-serif; }
  .flyer { position: relative; width: 848px; height: 1200px; overflow: hidden; background: var(--white); }

  .photo {
    position: absolute; left: 0; top: 0; width: 848px; height: 740px;
    background: radial-gradient(ellipse at 65% 45%, var(--photo-mid) 0%, #d6e0ec 40%, var(--photo-light) 80%);
  }
  .shapes { position: absolute; left: 0; top: 0; }

  .headline { position: absolute; left: 34px; top: 30px; color: var(--white); }
  .headline__lead { font-size: 18px; font-weight: 400; }
  .headline__main { font-size: 31px; font-weight: 600; margin-top: 4px; letter-spacing: 0.2px; }
  .headline__tail { font-size: 18px; font-weight: 400; margin-top: 8px; }

  .features { position: absolute; left: 0; top: 469px; list-style: none; }
  .features__item {
    width: 198px; height: 40px; margin-bottom: 7.5px;
    padding-left: 19px; color: var(--white);
    font-size: 26px; font-weight: 500; line-height: 40px;
  }
  .features__item--red { background: var(--red); }
  .features__item--navy { background: var(--navy); }

  .offer { position: absolute; right: 27px; top: 686px; text-align: right; color: var(--white); }
  .offer__intro { font-size: 18px; font-weight: 500; }
  .offer__title { font-size: 39px; font-weight: 500; margin-top: 2px; letter-spacing: 0.3px; }
  .offer__sub { font-size: 18px; font-weight: 400; margin-top: 2px; }

  .plan {
    position: absolute; top: 820px; width: 230px; height: 108px;
    background: linear-gradient(#ffffff, #f3f3f3);
    border: 4px solid var(--red-soft); border-radius: 12px;
    box-shadow: 0 0 0 2px rgba(255,255,255,0.35);
    color: var(--ink); text-align: center;
  }
  .plan--basic { left: 308px; }
  .plan--plus { left: 592px; }
  .plan__speed { font-size: 31px; font-weight: 500; margin-top: 14px; }
  .plan__speed b { font-weight: 800; }
  .plan__speed small { font-size: 20px; font-weight: 500; }
  .plan__price { font-size: 20px; color: var(--red); font-weight: 500; margin-top: 4px; }
  .plan__price b { font-size: 29px; font-weight: 800; }
  .plan-divider { position: absolute; left: 553px; top: 860px; color: var(--white); font-size: 22px; }

  .rule { position: absolute; left: 308px; width: 512px; height: 1px; background: rgba(255,255,255,0.85); }
  .rule--top { top: 948px; }
  .rule--bottom { top: 1025px; }

  .terms { position: absolute; right: 28px; text-align: right; color: var(--white); white-space: nowrap; }
  .terms--free { top: 952px; font-size: 15px; font-weight: 500; }
  .terms--free .terms__big { font-size: 30px; font-weight: 400; }
  .terms--free b { font-size: 17px; font-weight: 700; }
  .terms--free small { font-size: 11.5px; }
  .terms--limited { top: 990px; font-size: 11.5px; font-weight: 500; }
  .terms--limited b { font-size: 15.5px; font-weight: 700; }

  .brand { position: absolute; left: 38px; top: 1066px; display: flex; align-items: center; gap: 12px; }
  .brand__mark { width: 34px; height: 34px; background: var(--red); }
  .brand__name { color: var(--navy); font-size: 25px; font-weight: 800; line-height: 1.05; letter-spacing: 0.3px; }

  .contact { position: absolute; left: 360px; top: 1073px; color: var(--ink); font-size: 14px; font-weight: 500; }
  .contact__row { margin-bottom: 6px; }
  .contact__phone { color: var(--red); font-size: 25px; font-weight: 400; }
  .contact__email { color: var(--red); font-size: 17px; font-weight: 600; }

  .web-bar {
    position: absolute; left: 360px; top: 1160px; width: 488px; height: 40px;
    background: var(--navy); border-top-left-radius: 10px;
    color: var(--white); font-size: 18px; font-weight: 500;
    padding-left: 26px; line-height: 40px; letter-spacing: 0.4px;
  }
</style>
</head>
<body>
<main class="flyer">
  <div class="photo" role="img" aria-label="Photo of a smiling businessman in a blue shirt and striped tie working at a laptop in a bright office"></div>

  <svg class="shapes" width="848" height="1200" viewBox="0 0 848 1200" aria-hidden="true">
    <polygon points="0,0 848,0 848,40 0,212" fill="var(--navy)"/>
    <polygon points="390,110 848,16 848,40 430,118" fill="#8a93c8" opacity="0.45"/>
    <polygon points="0,724 848,604 848,1128 0,944" fill="var(--red)"/>
    <polygon points="0,724 520,650 0,780" fill="var(--red-deep)"/>
    <polygon points="0,724 848,604 848,640 0,740" fill="var(--red-deep)" opacity="0.55"/>
  </svg>

  <header class="headline">
    <p class="headline__lead">Finally,</p>
    <h1 class="headline__main">The High Speed Internet</h1>
    <p class="headline__tail">You Deserve is here...</p>
  </header>

  <ul class="features">
    <li class="features__item features__item--red">Fiber Optic</li>
    <li class="features__item features__item--navy">High Speed</li>
    <li class="features__item features__item--red">Affordable</li>
    <li class="features__item features__item--navy">Reliable</li>
  </ul>

  <section class="offer">
    <p class="offer__intro">Kelva Route Networks offers</p>
    <h2 class="offer__title">Fiber Optic Internet Service</h2>
    <p class="offer__sub">bringing you faster internet to reduce wait time.</p>
  </section>

  <div class="plan plan--basic">
    <p class="plan__speed"><b>100</b> Mbits <small>for</small></p>
    <p class="plan__price">$<b>140</b> /month</p>
  </div>
  <span class="plan-divider">or</span>
  <div class="plan plan--plus">
    <p class="plan__speed"><b>150</b> Mbits <small>for</small></p>
    <p class="plan__price">$<b>190</b> /month</p>
  </div>

  <div class="rule rule--top"></div>
  <p class="terms terms--free"><span class="terms__big">Free</span> construction cost up to <b>$10,000</b>, <small>limited funds available.</small></p>
  <p class="terms terms--limited"><b>Limited time offer.</b> Must commit before funds run out.</p>
  <div class="rule rule--bottom"></div>

  <div class="brand">
    <span class="brand__mark"></span>
    <span class="brand__name">KELVA ROUTE<br>NETWORKS</span>
  </div>

  <address class="contact" style="font-style: normal;">
    <p class="contact__row">For More Details</p>
    <p class="contact__row">Call US : <span class="contact__phone">(555) 274-3619</span> or</p>
    <p class="contact__row">Mail US : <span class="contact__email">support@kelvaroute.net</span></p>
  </address>

  <div class="web-bar">www.kelvaroute.net</div>
</main>
</body>
</html>
```